Webdesign
Zielgruppe
Briefing für die neue Website von TELORI GmbH
Allgemeine Informationen:
Name des Unternehmens: TELORI GmbH
Branche: Maschinenbau
Zweck der Website: Eine Unternehmenswebsite, die informiert, was die Firma macht und es potenziellen Kunden oder Partnern ermöglicht, in Kontakt zu treten.
Zielgruppe:
Hauptzielgruppe: Anlagenbauer, Maschinenbauer, Anlagenbetreiber aus verschiedenen Branchen.
Design-Anforderungen: Die Zielgruppe erwartet Professionalität und Klarheit, also sollte die Website eine hohe Qualität, Professionalität und Benutzerfreundlichkeit reflektieren.
Design-Vorlieben:
Farbschema & Stil: Das Design sollte sich an den bereitgestellten Logos orientieren. Der gewünschte Stil ist modern und klar.
Inspirationsquellen: Die Logos des Unternehmens, die dem Briefing beigefügt werden.
Inhalt und Struktur:
Einseitiges Design: Die Website sollte nur eine Seite zum Herunterscrollen haben.
Unternehmensvorstellung: Ein kurzer Abschnitt, der beschreibt, wer TELORI GmbH ist und was das Unternehmen macht.
Leistungsübersicht: Eine klare Darstellung der Dienstleistungen oder Produkte, die TELORI GmbH anbietet. Dies kann durch Symbole, kurze Texte oder Bilder dargestellt werden.
Kontaktmöglichkeit: Ein Kontaktformular oder zumindest klare Kontaktinformationen (Telefon, E-Mail, Adresse), so dass Besucher leicht in Kontakt treten können.
Aufgabenstellung
siehe oben

```html
<!DOCTYPE html>
<html lang="de">
<head>
<meta charset="utf-8">
<title>TELORI GmbH – Maschinenbau</title>
<link rel="stylesheet" href="https://fonts.googleapis.com/css2?family=Teko:wght@400;500;600&family=Rubik:wght@400;500&display=swap">
<style>
:root{
  --red:#c1040d;
  --dark:#333333;
  --ink:#2b2b2b;
  --text:#444;
  --partner:#2a1a1a;
  --white:#fff;
}
*{margin:0;padding:0;box-sizing:border-box}
html,body{width:1200px;height:2668px;overflow:hidden;background:var(--white)}
body{position:relative;font-family:'Rubik',sans-serif;color:var(--text)}
.abs{position:absolute}
.head{font-family:'Teko',sans-serif;font-weight:500;color:var(--ink);line-height:1}
/* top bar */
.topbar{left:0;top:0;width:1200px;height:37px;background:var(--dark);color:#eee;font-size:10px}
.topbar .item{position:absolute;top:12px;display:flex;align-items:center;gap:12px;white-space:nowrap}
.social{position:absolute;top:7px;width:22px;height:22px;border-radius:50%;background:var(--red)}
/* header */
.header{left:0;top:37px;width:1200px;height:63px;background:#fff;border-bottom:1px solid #eee}
.brand{position:absolute;left:222px;top:20px;display:flex;align-items:center;gap:8px;font-family:'Teko',sans-serif;font-size:26px;font-weight:600;color:var(--red)}
.brand .mark{width:16px;height:16px;border-radius:50%;background:var(--red)}
.nav{position:absolute;top:29px;font-size:10px;font-weight:500;color:var(--ink)}
.call{position:absolute;top:18px}
.call b{display:block;font-family:'Teko',sans-serif;font-weight:500;font-size:17px;color:var(--ink);line-height:1}
.call span{font-size:10px;color:var(--ink)}
/* hero */
.hero{left:0;top:100px;width:1200px;height:613px;background:linear-gradient(100deg,#1b1a1f 0%,#4a3222 35%,#7a4a26 55%,#3a2a26 75%,#1c1c22 100%)}
.hero-title{left:210px;top:180px;font-family:'Teko',sans-serif;font-weight:500;font-size:58px;line-height:86px;color:#fff;white-space:nowrap}
.hero-title .accent{color:var(--red)}
.hero-sub{left:218px;top:434px;width:330px;font-size:12px;font-weight:500;color:#fff;line-height:14px}
.btn{background:var(--red);color:#fff;font-family:'Teko',sans-serif;font-weight:500;letter-spacing:1px;display:flex;align-items:center;justify-content:center;gap:7px}
/* features */
.feature h3{font-family:'Teko',sans-serif;font-weight:500;font-size:22px;color:var(--ink)}
.feature p{font-size:10px;line-height:12px;width:180px;margin-top:6px}
.cta{left:746px;top:663px;width:188px;height:161px;background:var(--red);color:#fff;padding:26px 17px}
.cta h4{font-family:'Teko',sans-serif;font-weight:500;font-size:16px;line-height:23px}
.cta p{font-size:9.5px;line-height:12px;margin-top:8px}
/* about */
.about-img{left:197px;top:941px;width:393px;height:393px;background:linear-gradient(135deg,#5a6370,#8a8f95 40%,#a86b3a 60%,#3a3f44)}
.badge{left:208px;top:1221px;width:174px;height:100px;background:var(--red);color:#fff}
.label{font-family:'Teko',sans-serif;font-weight:500;color:var(--red);font-size:15px}
.about-p{left:622px;width:322px;font-size:10px;line-height:20.6px;color:var(--text)}
/* partners */
.partner{position:absolute;top:1446px;width:126px;height:38px;display:flex;align-items:center;gap:8px;font-family:'Rubik',sans-serif;font-weight:500;font-size:11px;line-height:12px;color:var(--partner);letter-spacing:.8px;text-transform:uppercase;white-space:nowrap}
.partner i{display:block;flex:none;width:32px;height:32px;border-radius:50%;background:var(--partner)}
/* services */
.card{width:256px;height:216px;border:2px solid var(--red);text-align:center;padding:0 30px}
.card h3{font-family:'Teko',sans-serif;font-weight:500;font-size:22px;line-height:29px;color:var(--ink)}
.card p{font-size:10px;line-height:12px;margin-top:6px}
.card svg{display:block;margin:0 auto}
.card.active{background:var(--red);border-color:var(--red)}
.card.active h3,.card.active p{color:#fff}
/* contact */
.field{left:640px;width:348px;border:1px solid var(--red);font-size:10px;color:#666;padding:9px 7px}
.info{left:226px;font-size:10px;color:var(--ink);line-height:13px}
.footer{left:0;top:2629px;width:1200px;height:39px;background:var(--dark);color:#eee;font-size:10px}
</style>
</head>
<body>

<div class="abs topbar">
  <div class="item" style="left:223px">
    <svg width="12" height="14" viewBox="0 0 12 14"><path d="M6 0a5 5 0 0 0-5 5c0 4 5 9 5 9s5-5 5-9a5 5 0 0 0-5-5zm0 7a2 2 0 1 1 0-4 2 2 0 0 1 0 4z" fill="#c1040d"/></svg>
    <span>Lindenweg 48, 54321 Feldstadt</span>
  </div>
  <div class="item" style="left:428px">
    <svg width="14" height="14" viewBox="0 0 14 14"><path d="M13 1 1 6l5 2 2 5z M6 8l7-7" fill="none" stroke="#c1040d" stroke-width="1.3"/></svg>
    <span>kontakt@telori-gmbh.de</span>
  </div>
  <div class="social" style="left:913px"></div>
  <div class="social" style="left:942px"></div>
  <div class="social" style="left:971px"></div>
  <div class="social" style="left:1000px"></div>
</div>

<div class="abs header">
  <div class="brand"><span class="mark"></span>TELORI</div>
  <div class="nav" style="left:647px">Home</div>
  <div class="nav" style="left:686px">About Us</div>
  <div class="nav" style="left:747px">Services</div>
  <div class="nav" style="left:813px">Contact Us</div>
  <svg class="abs" style="left:913px;top:20px" width="26" height="26" viewBox="0 0 24 24"><path d="M5 2h4l2 5-3 2a11 11 0 0 0 7 7l2-3 5 2v4a2 2 0 0 1-2 2A19 19 0 0 1 3 4a2 2 0 0 1 2-2z" fill="none" stroke="#c1040d" stroke-width="1.4"/></svg>
  <div class="call" style="left:947px"><b>Call Us Now!</b><span>555-210-4870</span></div>
</div>

<div class="abs hero" role="img" aria-label="Fabrikhalle mit Arbeiter im Schutzhelm, von hinten gesehen"></div>
<div class="abs hero-title"><span class="accent">TELORI</span> GmbH -<br>Nachhaltige Fertigung für<br>eine bessere Zukunft</div>
<div class="abs hero-sub">Reduzierung von Umweltauswirkungen und Förderung sozialer Verantwortung</div>
<div class="abs btn" style="left:222px;top:513px;width:122px;height:38px;font-size:13px">Mehr erfahren
  <svg width="12" height="12" viewBox="0 0 12 12"><circle cx="6" cy="6" r="5" fill="none" stroke="#fff"/><path d="M3.5 6h5M6.5 4l2 2-2 2" fill="none" stroke="#fff"/></svg></div>

<svg class="abs" style="left:202px;top:731px" width="40" height="40" viewBox="0 0 40 40"><path d="M4 36 26 14M30 4l6 6-8 8-6-6zM4 4l10 2 22 28-4 2L6 14z" fill="none" stroke="#c1040d" stroke-width="3" stroke-linejoin="round"/></svg>
<div class="abs feature" style="left:266px;top:740px"><h3>Efficient Processes</h3><p>Lorem ipsum dolor sit amet elit ut elit tellus luctus nec ullamcorper mattis pulvinar dapibus leo.</p></div>
<div class="abs feature" style="left:541px;top:740px"><h3>Fokus auf Qualität</h3><p>Lorem ipsum dolor sit amet elit ut elit tellus luctus nec ullamcorper mattis pulvinar dapibus leo.</p></div>
<div class="abs cta"><h4>Bereit, Ihre Fertigung auf die nächste Stufe zu heben?</h4><p>Lorem ipsum dolor sit amet consectetur adipiscing elit ut elit tellus.</p>
  <div style="margin-top:10px;font-family:'Teko',sans-serif;font-weight:500;font-size:13px;letter-spacing:1px;display:flex;align-items:center;gap:5px">Contact Us <svg width="12" height="12" viewBox="0 0 12 12"><circle cx="6" cy="6" r="5" fill="none" stroke="#fff"/><path d="M3.5 6h5M6.5 4l2 2-2 2" fill="none" stroke="#fff"/></svg></div></div>

<div class="abs about-img" role="img" aria-label="Roboter-Fertigungsanlage in einer Industriehalle"></div>
<div class="abs badge">
  <svg class="abs" style="left:10px;top:22px" width="48" height="44" viewBox="0 0 48 44"><path d="M2 2v40h44" fill="none" stroke="#fff" stroke-width="2.5"/><path d="M8 32l10-10 8 6 14-16" fill="none" stroke="#fff" stroke-width="2.5"/><circle cx="18" cy="22" r="2.5" fill="#fff"/><circle cx="26" cy="28" r="2.5" fill="#fff"/><circle cx="40" cy="12" r="2.5" fill="#fff"/></svg>
  <div class="abs" style="left:70px;top:18px;font-family:'Teko',sans-serif;font-weight:600;font-size:46px;line-height:1">25 +</div>
  <div class="abs" style="left:72px;top:66px;font-family:'Teko',sans-serif;font-weight:500;font-size:16px">Year Experience</div>
</div>
<div class="abs label" style="left:622px;top:952px">Über uns</div>
<div class="abs head" style="left:622px;top:973px;font-size:30px;line-height:43px">Willkommen bei TELORI GmbH - Ihr<br>Partner für Maschinenbau</div>
<div class="abs about-p" style="top:1079px">Die TELORI GmbH ist ein renommiertes Maschinenbauunternehmen, das sich auf die Entwicklung und Herstellung hochwertiger Maschinen und Anlagen spezialisiert hat. Mit jahrzehntelanger Erfahrung und einem engagierten Team von Ingenieuren und Fachleuten setzen wir Maßstäbe in der Branche.</div>
<div class="abs about-p" style="top:1200px">Die TELORI GmbH ist ein renommiertes Maschinenbauunternehmen, das sich auf die Entwicklung und Herstellung hochwertiger Maschinen und Anlagen spezialisiert hat. Mit jahrzehntelanger Erfahrung und einem engagierten Team von Ingenieuren und Fachleuten setzen wir Maßstäbe in der Branche.</div>

<div class="partner" style="left:205px"><i></i><span>Velnor<br>Studio</span></div>
<div class="partner" style="left:341px"><i></i><span>Harbora</span></div>
<div class="partner" style="left:480px"><i></i><span>Pixalune</span></div>
<div class="partner" style="left:614px"><i></i><span>Kestrum</span></div>
<div class="partner" style="left:757px"><i></i><span>Brandel<br>Group</span></div>
<div class="partner" style="left:891px"><i></i><span>Orvex<br>Media</span></div>

<div class="abs label" style="left:0;width:1200px;text-align:center;top:1576px">OUR SERVICES</div>
<div class="abs head" style="left:0;width:1200px;text-align:center;top:1606px;font-size:30px">Creating Solutions Tailored to Your Needs</div>
<div class="abs" style="left:0;width:1200px;text-align:center;top:1646px;font-size:10px">Lorem ipsum dolor sit amet consectetur adipiscing elit mauris molestie orci eget condimentum sollicitudin felis orci.</div>

<div class="abs card" style="left:197px;top:1698px;padding-top:30px">
  <svg width="30" height="30" viewBox="0 0 30 30"><path d="M3 3v24h24zM9 21h6l-6-6zM20 5l5 5-4 4-5-5z" fill="none" stroke="#c1040d" stroke-width="1.5"/></svg>
  <h3 style="margin-top:14px">Kundenspezifische<br>Maschinen</h3>
  <p>Wir entwerfen und bauen maßgeschneiderte Maschinen und Anlagen, die Ihren individuellen Anforderungen entsprechen.</p></div>
<div class="abs card" style="left:472px;top:1698px;padding-top:36px">
  <svg width="26" height="26" viewBox="0 0 26 26"><circle cx="10" cy="10" r="4" fill="none" stroke="#c1040d" stroke-width="1.5"/><circle cx="10" cy="10" r="7" fill="none" stroke="#c1040d" stroke-width="1.5" stroke-dasharray="3 2"/><circle cx="19" cy="19" r="4" fill="none" stroke="#c1040d" stroke-width="1.5" stroke-dasharray="2 1.5"/></svg>
  <h3 style="margin-top:18px">Prototypenentwicklung</h3>
  <p>Von der Idee bis zur Umsetzung - wir unterstützen Sie bei der Entwicklung von Prototypen für neue Maschinen und Produkte.</p></div>
<div class="abs card" style="left:746px;top:1698px;padding-top:36px">
  <svg width="26" height="30" viewBox="0 0 26 30"><path d="M2 2h14l6 6v20H2zM16 2v6h6M6 12h10M6 16h6" fill="none" stroke="#c1040d" stroke-width="1.5"/><circle cx="19" cy="23" r="3" fill="#fff" stroke="#c1040d" stroke-width="1.5"/><path d="M21 25l3 3" stroke="#c1040d" stroke-width="1.5"/></svg>
  <h3 style="margin-top:14px">Prototypenentwicklung</h3>
  <p>Von der Idee bis zur Umsetzung - wir unterstützen Sie bei der Entwicklung von Prototypen für neue Maschinen und Produkte.</p></div>

<div class="abs card" style="left:197px;top:1938px;padding-top:34px">
  <svg width="28" height="28" viewBox="0 0 28 28"><path d="M3 25 25 3M3 3l22 22M6 3l19 19M3 6l19 19" fill="none" stroke="#c1040d" stroke-width="1.5"/></svg>
  <h3 style="margin-top:20px">Wartung und Reparatur</h3>
  <p>Unser Service-Team steht Ihnen zur Verfügung, um die reibungslose Funktion Ihrer Maschinen zu gewährleisten und im Falle von Problemen schnell zu handeln.</p></div>
<div class="abs card" style="left:472px;top:1938px;padding-top:82px">
  <h3>Technische Beratung</h3>
  <p>Wir bieten umfassende Beratungsdienstleistungen, um Ihnen bei der Auswahl der richtigen Maschinenlösungen zu helfen.</p></div>
<div class="abs card active" style="left:746px;top:1938px;padding-top:32px">
  <svg width="32" height="32" viewBox="0 0 32 32"><circle cx="16" cy="16" r="16" fill="#fff"/><path d="M16 9a5 5 0 0 0-3 9v2h6v-2a5 5 0 0 0-3-9zM13 22h6" fill="none" stroke="#c1040d" stroke-width="1.6"/></svg>
  <h3 style="margin-top:18px">Prototype Development</h3>
  <p>Lorem ipsum dolor sit amet elit ut elit tellus luctus nec ullamcorper mattis pulvinar dapibus leo.</p></div>

<div class="abs head" style="left:197px;top:2229px;font-size:30px">Kontaktinformationen</div>
<svg class="abs" style="left:196px;top:2298px" width="13" height="16" viewBox="0 0 12 14"><path d="M6 0a5 5 0 0 0-5 5c0 4 5 9 5 9s5-5 5-9a5 5 0 0 0-5-5zm0 7a2 2 0 1 1 0-4 2 2 0 0 1 0 4z" fill="#c1040d"/></svg>
<div class="abs info" style="top:2301px">Lindenweg 48,<br>&nbsp;54321 Feldstadt</div>
<svg class="abs" style="left:194px;top:2338px" width="16" height="16" viewBox="0 0 14 14"><path d="M13 1 1 6l5 2 2 5z M6 8l7-7" fill="none" stroke="#c1040d" stroke-width="1.3"/></svg>
<div class="abs info" style="top:2340px">kontakt@telori-gmbh.de</div>
<svg class="abs" style="left:194px;top:2372px" width="16" height="16" viewBox="0 0 24 24"><path d="M5 2h4l2 5-3 2a11 11 0 0 0 7 7l2-3 5 2v4a2 2 0 0 1-2 2A19 19 0 0 1 3 4a2 2 0 0 1 2-2z" fill="none" stroke="#c1040d" stroke-width="2"/></svg>
<div class="abs info" style="top:2374px">+49 30 98 76 54 32</div>

<div class="abs head" style="left:646px;top:2225px;font-size:30px">Get In Touch</div>
<div class="abs field" style="top:2261px;height:30px">Name</div>
<div class="abs field" style="top:2297px;height:30px">Email</div>
<div class="abs field" style="top:2332px;height:30px">Subject</div>
<div class="abs field" style="top:2368px;height:61px">Message</div>
<div class="abs btn" style="left:640px;top:2434px;width:348px;height:38px;font-size:13px">Send Message</div>

<div class="abs footer">
  <span class="abs" style="left:198px;top:14px">Privacy Policy</span>
  <span class="abs" style="left:335px;top:14px">Terms &amp; Service</span>
  <span class="abs" style="left:721px;top:14px">Copyright 2023 © All Right Reserved Design</span>
</div>

</body>
</html>
```